Business Card Design Project

Please create a custom business card for Plume tallying. The logo is attached to this brief.

Questions can be posted on the Discussion Board.

Address :
CEO : Gerhard Moulin
Mobile : +33641927058
9 rue Vasselot
75014 Paris
France

Reason: Sorry wrong logo. I will update asap

Hi, Sorry, I post the wrong file. I just update the correct logo. If you can integrate some charts as background it will be nice

Hi Everybody Please make it beautifull, clean, soft like quince designs does to create their product. I want somewhere to show in a beautifull way some datavisualization charts. Not to much, but try to find a way to design it beautifull with less. Get inspire by datavisualization : http://www.brovaxkit.com/27841-neat-vector-chart-and-graph-layout-pieces-07/

Target Market(s)

B to B
Customers are accountant, CPA, finance departement

Industry/Entity Type

Business

Font styles to use
Sans Serif

Requirements
Must have
• I want to give a clear message about what we do. We do dashboards, we create beautifull charts
Nice to have
• displays charts icons to let people know tha we do charts

```html
<!DOCTYPE html>
<html lang="en">
<head>
<meta charset="utf-8">
<title>Plume tallying – Business Card</title>
<link href="https://fonts.googleapis.com/css2?family=Open+Sans:wght@300&family=Michroma&display=swap" rel="stylesheet">
<style>
  :root {
    --backdrop: #2b2b2b;
    --card-dark: #0c0c0d;
    --card-light: #cfcdcd;
    --brand-blue: #17a9e1;
    --ink-light: #d8d8d8;
    --ink-dark: #3a3a3a;
  }
  html, body {
    margin: 0;
    padding: 0;
    width: 1200px;
    height: 1134px;
    overflow: hidden;
    background: var(--backdrop);
  }
  .canvas {
    position: relative;
    width: 1200px;
    height: 1134px;
  }
  .card {
    position: absolute;
    overflow: hidden;
    box-shadow: 0 10px 24px rgba(0,0,0,.55);
  }
  .card--front { background: linear-gradient(160deg, #1a1b1d, var(--card-dark) 70%); }
  .card--back { background: radial-gradient(circle at 45% 40%, #f4f4f4, var(--card-light) 75%); }

  .band {
    position: absolute;
    background: var(--brand-blue);
  }

  .brand {
    position: absolute;
    display: flex;
    align-items: center;
  }
  .brand__dot {
    border-radius: 50%;
    background: var(--brand-blue);
    flex: none;
  }
  .brand__name {
    font-family: "Open Sans", sans-serif;
    font-weight: 300;
    line-height: 1;
    white-space: nowrap;
  }
  .brand--on-dark .brand__name { color: var(--ink-light); }
  .brand--on-light .brand__name { color: var(--ink-dark); }

  .divider {
    position: absolute;
    background: var(--brand-blue);
  }

  .contact {
    position: absolute;
    width: max-content;
    font-family: "Michroma", sans-serif;
    color: var(--ink-light);
    text-transform: uppercase;
  }
  .contact__name { letter-spacing: .04em; white-space: nowrap; }
  .contact__role { text-align: right; opacity: .8; }
  .contact__line { display: flex; align-items: center; white-space: nowrap; }
  .contact__line svg { flex: none; fill: var(--ink-light); }
  .contact__indent { white-space: nowrap; }

  /* large front */
  .front-lg { left: 50px; top: 110px; width: 580px; height: 330px; }
  .front-lg .band--top { left: 40px; right: 40px; top: 24px; height: 22px; }
  .front-lg .band--bottom { left: 40px; right: 40px; bottom: 24px; height: 22px; }
  .front-lg .brand { left: 40px; top: 130px; gap: 12px; }
  .front-lg .brand__dot { width: 66px; height: 66px; }
  .front-lg .brand__name { font-size: 26px; }
  .front-lg .divider { left: 298px; top: 90px; width: 3px; height: 150px; }
  .front-lg .contact { left: 316px; top: 108px; }
  .front-lg .contact__name { font-size: 15px; }
  .front-lg .contact__role { font-size: 9px; margin: 4px 0 12px; }
  .front-lg .contact__line { font-size: 10px; gap: 8px; margin-bottom: 5px; }
  .front-lg .contact__indent { font-size: 10px; padding-left: 20px; margin-bottom: 5px; }

  /* large back */
  .back-lg { left: 660px; top: 110px; width: 500px; height: 330px; }
  .back-lg .brand { left: 50%; top: 50%; transform: translate(-50%, -50%); gap: 18px; }
  .back-lg .brand__dot { width: 110px; height: 110px; }
  .back-lg .brand__name { font-size: 40px; }

  /* logo lockup */
  .lockup { left: 45px; top: 888px; gap: 24px; }
  .lockup .brand__dot { width: 205px; height: 205px; }
  .lockup .brand__name { font-size: 58px; color: var(--ink-dark); }

  /* small front */
  .front-sm { left: 655px; top: 912px; width: 232px; height: 140px; }
  .front-sm .band--top { left: 14px; right: 14px; top: 12px; height: 9px; }
  .front-sm .band--bottom { left: 14px; right: 14px; bottom: 12px; height: 9px; }
  .front-sm .brand { left: 14px; top: 60px; gap: 5px; }
  .front-sm .brand__dot { width: 22px; height: 22px; }
  .front-sm .brand__name { font-size: 10px; }
  .front-sm .divider { left: 112px; top: 40px; width: 1px; height: 60px; }
  .front-sm .contact { left: 118px; top: 47px; }
  .front-sm .contact__name { font-size: 6px; }
  .front-sm .contact__role { font-size: 3.5px; margin: 1px 0 4px; }
  .front-sm .contact__line { font-size: 4px; gap: 3px; margin-bottom: 2px; }
  .front-sm .contact__indent { font-size: 4px; padding-left: 9px; margin-bottom: 2px; }

  /* small back */
  .back-sm { left: 912px; top: 914px; width: 248px; height: 148px; }
  .back-sm .brand { left: 50%; top: 50%; transform: translate(-50%, -50%); gap: 8px; }
  .back-sm .brand__dot { width: 52px; height: 52px; }
  .back-sm .brand__name { font-size: 16px; }
</style>
</head>
<body>
<main class="canvas">

  <section class="card card--front front-lg" aria-label="Card front">
    <div class="band band--top"></div>
    <div class="brand brand--on-dark">
      <span class="brand__dot"></span>
      <span class="brand__name">Plume tallying</span>
    </div>
    <div class="divider"></div>
    <div class="contact">
      <div class="contact__name">Gerhard Moulin</div>
      <div class="contact__role">C.E.O</div>
      <div class="contact__line">
        <svg width="12" height="12" viewBox="0 0 12 12" aria-hidden="true"><rect x="1" y="0" width="10" height="12" rx="2"/><rect x="3" y="2" width="6" height="6" fill="#0c0c0d"/></svg>
        +33641927058
      </div>
      <div class="contact__line">
        <svg width="12" height="12" viewBox="0 0 12 12" aria-hidden="true"><path d="M6 0a4 4 0 0 1 4 4c0 3-4 8-4 8S2 7 2 4a4 4 0 0 1 4-4z"/><circle cx="6" cy="4" r="1.5" fill="#0c0c0d"/></svg>
        9 rue Vasselot
      </div>
      <div class="contact__indent">75014 Paris</div>
      <div class="contact__indent">France</div>
    </div>
    <div class="band band--bottom"></div>
  </section>

  <section class="card card--back back-lg" aria-label="Card back">
    <div class="brand brand--on-light">
      <span class="brand__dot"></span>
      <span class="brand__name">Plume tallying</span>
    </div>
  </section>

  <div class="brand brand--on-light lockup">
    <span class="brand__dot"></span>
    <span class="brand__name">Plume tallying</span>
  </div>

  <section class="card card--front front-sm" aria-label="Card front, small">
    <div class="band band--top"></div>
    <div class="brand brand--on-dark">
      <span class="brand__dot"></span>
      <span class="brand__name">Plume tallying</span>
    </div>
    <div class="divider"></div>
    <div class="contact">
      <div class="contact__name">Gerhard Moulin</div>
      <div class="contact__role">C.E.O</div>
      <div class="contact__line">
        <svg width="6" height="6" viewBox="0 0 12 12" aria-hidden="true"><rect x="1" y="0" width="10" height="12" rx="2"/></svg>
        +33641927058
      </div>
      <div class="contact__line">
        <svg width="6" height="6" viewBox="0 0 12 12" aria-hidden="true"><path d="M6 0a4 4 0 0 1 4 4c0 3-4 8-4 8S2 7 2 4a4 4 0 0 1 4-4z"/></svg>
        9 rue Vasselot
      </div>
      <div class="contact__indent">75014 Paris</div>
      <div class="contact__indent">France</div>
    </div>
    <div class="band band--bottom"></div>
  </section>

  <section class="card card--back back-sm" aria-label="Card back, small">
    <div class="brand brand--on-light">
      <span class="brand__dot"></span>
      <span class="brand__name">Plume tallying</span>
    </div>
  </section>

</main>
</body>
</html>
```